Brightmoor Academy - Personal Development business 2.0 needs a social post format design.

https://www.brightmooracademy.example

Our focus with Brightmoor Academy is on developing people through knowledge and skills to improve their everyday lives.
We love simplicity, Quorel design and less is more.

We are crazy about personal growth, science, design, the latest gadgets and people.

We need 4 formats for our social media posts.
1. Blogs -to pronounce a blog post
2. Workshop /training - to pronounce our workshops/trainings (both online and offline)
3. Podcast - called "Wissel je blik". To pronounce a guest we've spoken. The host is called Berend.
4. Facts - to pronounce short facts about personal development. Invites people to read more.
The formats should include: high quality pictogram (better than the uploaded picto's), 1 of the 3 logo's in the design.
It's important that we can edit the design in Lumora Draw / Lumora Pixel to adjust the text in the format.

Attached you find four of our current designs, which are a poor example of how the designs should look like. These are just to show you how much lines of text (more or less) will be in the designs. So please do not make a design that looks like these ;) You have carte blanche.

Our customers are mostly women (80%). We focus on both business and casual customers.

Target Market(s)

80% woman, 20% men. We focus on both business and casual customers.

Requirements
Must have
• Less is more. Quorel Design alike. Simplicity.
Aimed at the women target audience.
Designs must be edible for adjusting the text in the format.
Nice to have
• Unique concept.
The design should "breathe".
Each design can have a different color, so customers identify the specific post with specific information. For example, blog is red, workshop post black, etc.

```html
<!DOCTYPE html>
<html lang="nl">
<head>
<meta charset="utf-8">
<title>Brightmoor Academy – social post formats</title>
<link rel="stylesheet" href="https://fonts.googleapis.com/css2?family=Montserrat:wght@400;500;600;700;800&display=swap">
<style>
  :root {
    --stage: #b3ffe0;
    --ink: #0a0a0a;
    --white: #ffffff;
    --ring: #f1f1f1;
    --podcast: #4e94d4;
    --blog: #f29807;
    --training: #000000;
    --facts: #267c08;
    --plate: #d7192b;
    --magenta: #c21fbf;
    --cyan: #1aa0e6;
    --photo-warm-a: #f4efe9;
    --photo-warm-b: #c9a774;
    --photo-warm-c: #1f2f55;
    --photo-dark-a: #f3f3f3;
    --photo-dark-b: #8b6650;
    --photo-dark-c: #1b1b1d;
  }
  * { box-sizing: border-box; margin: 0; padding: 0; }
  html, body { width: 1200px; height: 857px; overflow: hidden; }
  body {
    background: var(--stage);
    font-family: "Montserrat", Arial, sans-serif;
    position: relative;
  }
  .sheet-title {
    position: absolute; top: 24px; left: 0; width: 1200px;
    text-align: center; font-size: 26px; font-weight: 700;
    color: var(--ink); letter-spacing: 0.5px;
  }
  .post {
    position: absolute; width: 348px; height: 347px;
    overflow: hidden; color: var(--white);
  }
  .post--podcast { left: 228px; top: 95px; background: var(--podcast); }
  .post--blog { left: 594px; top: 95px; background: var(--blog); }
  .post--training { left: 228px; top: 465px; background: var(--training); }
  .post--facts { left: 594px; top: 465px; background: var(--facts); }

  .post::before, .post::after {
    content: ""; position: absolute; top: 4px; bottom: 4px; width: 0;
    border-left: 1.5px dotted rgba(255,255,255,0.55);
  }
  .post::before { left: 6px; }
  .post::after { right: 6px; }

  .post-label {
    position: absolute; left: 25px; top: 26px;
    display: flex; align-items: center; gap: 4px;
    font-size: 11px; font-weight: 700; letter-spacing: 0.2px;
  }
  .post-label svg { width: 17px; height: 17px; }

  .post-frame { position: absolute; left: 0; top: 0; width: 348px; height: 347px; }

  .post-photo {
    position: absolute; left: 84px; top: 60px; width: 180px; height: 180px;
    border-radius: 50%;
  }
  .post--podcast .post-photo, .post--blog .post-photo {
    background: radial-gradient(circle at 50% 30%, var(--photo-warm-b) 0 22%, transparent 23%),
                linear-gradient(180deg, var(--photo-warm-a) 0 58%, var(--photo-warm-c) 58% 100%);
  }
  .post--training .post-photo, .post--facts .post-photo {
    background: radial-gradient(circle at 50% 28%, var(--photo-dark-b) 0 20%, transparent 21%),
                linear-gradient(180deg, var(--photo-dark-a) 0 55%, var(--photo-dark-c) 55% 100%);
  }

  .post-nameplate {
    position: absolute; left: 91px; top: 175px; width: 169px; height: 36px;
    background: linear-gradient(90deg, var(--plate) 0%, var(--plate) 55%, rgba(215,25,43,0.15) 100%);
    clip-path: polygon(0 0, 96% 0, 100% 100%, 0 100%);
    text-align: center; padding-top: 4px;
  }
  .post-nameplate .name { display: block; font-size: 16px; font-weight: 800; line-height: 17px; text-transform: uppercase; }
  .post-nameplate .role { display: block; font-size: 8px; font-weight: 500; line-height: 10px; text-transform: uppercase; }

  .post-headline { position: absolute; left: 0; width: 348px; text-align: center; }
  .headline-lead { display: block; font-size: 18px; font-weight: 500; line-height: 22px; }
  .headline-main { display: block; font-size: 25px; font-weight: 800; line-height: 28px; }
  .headline-bold { display: block; font-size: 18px; font-weight: 800; line-height: 24px; }
  .headline-sub { display: block; font-size: 14px; font-weight: 500; line-height: 18px; letter-spacing: 0.3px; }
  .headline-quote { display: block; font-size: 16.5px; font-weight: 800; line-height: 21px; }

  .post-brand {
    position: absolute; right: 22px; top: 305px;
    font-size: 10px; font-weight: 600; color: var(--white);
  }

  .decor-dots { position: absolute; width: 4px; }
  .decor-dots i { display: block; width: 3px; height: 3px; border-radius: 50%; margin-bottom: 2.5px; background: currentColor; }
  .decor-dots--magenta { left: 24px; top: 74px; color: var(--magenta); }
  .decor-dots--cyan { left: 309px; top: 228px; color: var(--cyan); }
  .decor-dots--light { left: 24px; top: 306px; color: rgba(255,255,255,0.6); }
  .decor-ring { position: absolute; width: 6px; height: 6px; border-radius: 50%; border: 1.2px solid; }
  .decor-ring--cyan { left: 295px; top: 80px; border-color: var(--cyan); }
  .decor-ring--magenta { left: 54px; top: 234px; border-color: var(--magenta); }
</style>
</head>
<body>

<h1 class="sheet-title">IMAGES CAN BE REPLACED BY YOUR OWN</h1>

<!-- Podcast -->
<section class="post post--podcast">
  <div class="post-label">
    <svg viewBox="0 0 24 24" fill="none" stroke="#fff" stroke-width="2" stroke-linecap="round"><circle cx="12" cy="10" r="9"/><circle cx="12" cy="10" r="5"/><rect x="10" y="8" width="4" height="14" rx="2" fill="#fff"/></svg>
    PODCAST
  </div>
  <svg class="post-frame" viewBox="0 0 348 347">
    <circle cx="174" cy="150" r="92" fill="none" stroke="var(--ring)" stroke-width="5"/>
    <path d="M120 66 A100 100 0 0 0 91 206" fill="none" stroke="#fff" stroke-width="2.5"/>
    <path d="M228 66 A100 100 0 0 1 257 206" fill="none" stroke="#fff" stroke-width="2.5"/>
  </svg>
  <div class="post-photo" role="img" aria-label="Portretfoto van de podcastgast met koptelefoon"></div>
  <div class="post-nameplate"><span class="name">Mirel Stam</span><span class="role">Podcast gueast</span></div>
  <span class="decor-dots decor-dots--magenta"><i></i><i></i><i></i><i></i></span>
  <span class="decor-dots decor-dots--cyan"><i></i><i></i><i></i><i></i></span>
  <span class="decor-dots decor-dots--light"><i></i><i></i><i></i><i></i></span>
  <span class="decor-ring decor-ring--cyan"></span>
  <span class="decor-ring decor-ring--magenta"></span>
  <div class="post-headline" style="top:244px">
    <span class="headline-lead">Wissel je blik met</span>
    <span class="headline-main">Joris van Dalen</span>
  </div>
  <div class="post-brand">Brightmoor Academy</div>
</section>

<!-- Blog -->
<section class="post post--blog">
  <div class="post-label">
    <svg viewBox="0 0 24 24" fill="none" stroke="#fff" stroke-width="2.2" stroke-linecap="round" stroke-linejoin="round"><path d="M4 20l4-1 11-11-3-3L5 16z"/><path d="M14 7l3 3"/></svg>
    BLOG
  </div>
  <svg class="post-frame" viewBox="0 0 348 347">
    <circle cx="174" cy="150" r="92" fill="none" stroke="var(--ring)" stroke-width="5"/>
    <path d="M120 66 A100 100 0 0 0 91 206" fill="none" stroke="#fff" stroke-width="2.5"/>
    <path d="M228 66 A100 100 0 0 1 257 206" fill="none" stroke="#fff" stroke-width="2.5"/>
  </svg>
  <div class="post-photo" role="img" aria-label="Portretfoto van de blogschrijver"></div>
  <div class="post-nameplate"><span class="name">Mirel Stam</span><span class="role">Blogpost writer</span></div>
  <span class="decor-dots decor-dots--magenta"><i></i><i></i><i></i><i></i></span>
  <span class="decor-dots decor-dots--cyan"><i></i><i></i><i></i><i></i></span>
  <span class="decor-dots decor-dots--light"><i></i><i></i><i></i><i></i></span>
  <span class="decor-ring decor-ring--cyan"></span>
  <span class="decor-ring decor-ring--magenta"></span>
  <div class="post-headline" style="top:245px">
    <span class="headline-bold">Goede voornemens</span>
    <span class="headline-bold">die je volhoudt - 3 tips</span>
  </div>
  <div class="post-brand">Brightmoor Academy</div>
</section>

<!-- Online training -->
<section class="post post--training">
  <div class="post-label">
    <svg viewBox="0 0 24 24" fill="none" stroke="#fff" stroke-width="1.8" stroke-linecap="round"><rect x="3" y="3" width="18" height="13" rx="2"/><circle cx="9" cy="8" r="2" fill="#fff"/><path d="M6 14v-2h6v2M13 9l4-3"/><path d="M3 22h6M11 22h4M17 22h4"/></svg>
    ONLINE TRAINING
  </div>
  <svg class="post-frame" viewBox="0 0 348 347">
    <circle cx="174" cy="150" r="92" fill="none" stroke="var(--ring)" stroke-width="5"/>
    <path d="M120 66 A100 100 0 0 0 91 206" fill="none" stroke="#fff" stroke-width="2.5"/>
    <path d="M228 66 A100 100 0 0 1 257 206" fill="none" stroke="#fff" stroke-width="2.5"/>
  </svg>
  <div class="post-photo" role="img" aria-label="Portretfoto van de trainer in pak"></div>
  <div class="post-nameplate"><span class="name">Joost Brand</span><span class="role">Online trainer</span></div>
  <span class="decor-dots decor-dots--magenta"><i></i><i></i><i></i><i></i></span>
  <span class="decor-dots decor-dots--cyan"><i></i><i></i><i></i><i></i></span>
  <span class="decor-dots decor-dots--light"><i></i><i></i><i></i><i></i></span>
  <span class="decor-ring decor-ring--cyan"></span>
  <span class="decor-ring decor-ring--magenta"></span>
  <div class="post-headline" style="top:245px">
    <span class="headline-main">Pre-New Year’s Eve</span>
    <span class="headline-sub">Dinsdag 29 December, 19-21u</span>
  </div>
  <div class="post-brand">Brightmoor Academy</div>
</section>

<!-- Facts -->
<section class="post post--facts">
  <div class="post-label">
    <svg viewBox="0 0 24 24" fill="none" stroke="#fff" stroke-width="1.8" stroke-linecap="round" stroke-linejoin="round"><path d="M12 21a9 9 0 1 0-7-3.4L4 22l4-1.6A9 9 0 0 0 12 21z"/><path d="M7 10h2l3-3v10l-3-3H7z" fill="#fff"/><path d="M15 9.5a3.5 3.5 0 0 1 0 5"/></svg>
    FACTS
  </div>
  <svg class="post-frame" viewBox="0 0 348 347">
    <circle cx="174" cy="150" r="92" fill="none" stroke="var(--ring)" stroke-width="5"/>
    <path d="M120 66 A100 100 0 0 0 91 206" fill="none" stroke="#fff" stroke-width="2.5"/>
    <path d="M228 66 A100 100 0 0 1 257 206" fill="none" stroke="#fff" stroke-width="2.5"/>
  </svg>
  <div class="post-photo" role="img" aria-label="Portretfoto van de feitenverstrekker in pak"></div>
  <div class="post-nameplate"><span class="name">Joost Brand</span><span class="role">Facts provider</span></div>
  <span class="decor-dots decor-dots--magenta"><i></i><i></i><i></i><i></i></span>
  <span class="decor-dots decor-dots--cyan"><i></i><i></i><i></i><i></i></span>
  <span class="decor-dots decor-dots--light"><i></i><i></i><i></i><i></i></span>
  <span class="decor-ring decor-ring--cyan"></span>
  <span class="decor-ring decor-ring--magenta"></span>
  <div class="post-headline" style="top:253px">
    <span class="headline-quote">“Gemiddeld haalt slechts 20%</span>
    <span class="headline-quote">zijn/haar goede voornemens”</span>
  </div>
  <div class="post-brand">Brightmoor Academy</div>
</section>

</body>
</html>
```